business card design for a plumbing contractor

i need a double business card for a plumbing business, our initial service is residential Sewer Drain Cleaning.

Target Market(s)

other plumbing Business

Industry/Entity Type

Plumbing

Contact Information for Business Card

www.PipeworksCrestline.example- 5817302946-

Font styles to use
Serif

Colors
ec1f27
0455a3

```html
<!DOCTYPE html>
<html lang="en">
<head>
<meta charset="utf-8">
<title>Pipeworks Crestline – Business Card</title>
<link rel="stylesheet" href="https://fonts.googleapis.com/css2?family=Montserrat:wght@400;500;600;700;800&display=swap">
<style>
  :root {
    --bg: #eceded;
    --card-white: #fbfbfb;
    --card-dark: #4c463b;
    --ink: #5a554d;
    --ink-soft: #6b665e;
    --red: #d7202a;
    --white: #ffffff;
  }
  * { margin: 0; padding: 0; box-sizing: border-box; }
  html, body {
    width: 1200px; height: 1019px; overflow: hidden;
    background: var(--bg);
    font-family: "Montserrat", sans-serif;
  }
  .sheet {
    width: 1200px; height: 1019px;
    display: flex; align-items: center; justify-content: center; gap: 40px;
  }
  .card {
    position: relative;
    width: 540px; height: 309px;
    border-radius: 3px;
    box-shadow: 0 6px 18px rgba(0,0,0,0.12);
    overflow: hidden;
  }
  /* front */
  .card--front { background: var(--card-white); color: var(--ink); }
  .brand { display: flex; align-items: center; gap: 8px; }
  .brand__mark { width: 14px; height: 14px; background: var(--red); flex: none; }
  .brand__name { font-weight: 800; letter-spacing: -0.2px; }
  .card--front .brand { position: absolute; left: 36px; top: 34px; }
  .card--front .brand__name { font-size: 22px; color: var(--ink); }
  .person { position: absolute; left: 62px; top: 84px; }
  .person__name { font-size: 15px; font-weight: 600; letter-spacing: 1.5px; color: var(--ink); }
  .person__role { font-size: 10px; font-weight: 500; color: var(--red); margin-top: 1px; }
  .contact { position: absolute; left: 36px; top: 130px; list-style: none; }
  .contact__item {
    display: flex; align-items: center; gap: 10px;
    font-size: 11.5px; color: var(--ink-soft); height: 21px;
  }
  .contact__icon { width: 13px; height: 13px; flex: none; }
  .social { position: absolute; right: 22px; bottom: 30px; display: flex; gap: 3px; }
  .social__tile { width: 14px; height: 14px; background: var(--red); }
  .stripe { position: absolute; left: 0; right: 0; bottom: 0; height: 10px; }
  .stripe__gray { position: absolute; left: 0; bottom: 0; width: 56%; height: 4px; background: var(--card-dark); }
  .stripe__red { position: absolute; left: 56%; right: 0; bottom: 0; height: 8px; background: var(--red); }
  /* back */
  .card--back { background: var(--card-dark); color: var(--white); }
  .card--back .brand { position: absolute; left: 0; right: 0; top: 108px; justify-content: center; }
  .card--back .brand__name { font-size: 28px; color: var(--white); }
  .card--back .brand__mark { width: 18px; height: 18px; }
  .tagline {
    position: absolute; left: 0; right: 0; top: 170px;
    text-align: center; font-size: 10.5px; letter-spacing: 0.6px; color: var(--white);
  }
</style>
</head>
<body>
<main class="sheet">
  <section class="card card--front">
    <div class="brand">
      <span class="brand__name">Pipeworks Crestline</span>
      <span class="brand__mark"></span>
    </div>
    <div class="person">
      <div class="person__name">DANIEL REYES</div>
      <div class="person__role">Managing Partner</div>
    </div>
    <ul class="contact">
      <li class="contact__item">
        <svg class="contact__icon" viewBox="0 0 16 16"><path fill="#d7202a" d="M4 1.5l2.3 3-1.4 1.6c.8 1.9 2.2 3.3 4.1 4.1l1.6-1.4 3 2.3-1.3 2.6C7.5 13.6 2.4 8.5 1.5 3.2z"/></svg>
        <span>5817302946</span>
      </li>
      <li class="contact__item">
        <svg class="contact__icon" viewBox="0 0 16 16"><rect x="1.5" y="3.5" width="13" height="9" fill="none" stroke="#d7202a" stroke-width="1.5"/><path d="M1.5 3.5l6.5 5 6.5-5" fill="none" stroke="#d7202a" stroke-width="1.5"/></svg>
        <span>Dispatcher@PipeworksCrestline.example</span>
      </li>
      <li class="contact__item">
        <svg class="contact__icon" viewBox="0 0 16 16"><g fill="none" stroke="#d7202a" stroke-width="1.3"><circle cx="8" cy="8" r="6.3"/><ellipse cx="8" cy="8" rx="2.8" ry="6.3"/><path d="M1.7 8h12.6"/></g></svg>
        <span>www.PipeworksCrestline.example</span>
      </li>
    </ul>
    <div class="social">
      <span class="social__tile"></span>
      <span class="social__tile"></span>
      <span class="social__tile"></span>
    </div>
    <div class="stripe">
      <span class="stripe__gray"></span>
      <span class="stripe__red"></span>
    </div>
  </section>

  <section class="card card--back">
    <div class="brand">
      <span class="brand__name">Pipeworks Crestline</span>
      <span class="brand__mark"></span>
    </div>
    <p class="tagline">Sewer Drain Cleaning • Maintenance • Trenchless Pipe Installs</p>
  </section>
</main>
</body>
</html>
```